Dalvor Inc Business Card

Looking to get an updated business card for a Contract Machining company (www.dalvorinc-example.com) - looking for a clean design the portrays the technical nature of the business - colors can follow the website design and be in any combination that makes sense (red black, white, metallic or silver) - logos attached for use also. Would like space for: Name, title, business phone (555 214-3098), cell phone , website (www.dalvorinc-example.com) - possibly QR code could be integrated for website (designer choice), business address - 418 Birchfield Lane, Maple Hollow, MI 49012 (cards will be for 4 employees, I will either need to modify a template or I can provide individual information)
Target Market(s)
Aerospace, defense and medical device manufacturing companies that need machining
Industry/Entity Type
Machining for aerospace, defense, medical
Contact Information for Business Card
Name, Title, Business Phone, Cell Phone, email, business website and business address

```html
<!DOCTYPE html>
<html lang="en">
<head>
<meta charset="utf-8">
<title>Dalvor Inc Business Card</title>
<link href="https://fonts.googleapis.com/css2?family=Arimo:wght@400;700&display=swap" rel="stylesheet">
<style>
  :root {
    --bg: #2a2a2c;
    --card-black: #1e1e20;
    --pattern-dark: #161617;
    --pattern-light: #3a3a3c;
    --brand-red: #b31b23;
    --white: #ffffff;
    --rule-grey: #8a8a8a;
  }
  * { margin: 0; padding: 0; box-sizing: border-box; }
  html, body {
    width: 1200px; height: 874px; overflow: hidden;
    background: var(--bg);
    font-family: "Arimo", Arial, sans-serif;
  }
  .card {
    position: absolute; left: 300px;
    width: 600px; height: 343px;
    border-radius: 18px; overflow: hidden;
    box-shadow: 0 10px 30px rgba(0,0,0,.45);
  }
  .card--back { top: 64px; background: var(--card-black); }
  .pattern-field {
    position: absolute; inset: 0;
    background: linear-gradient(100deg, var(--pattern-dark) 0%, #232325 55%, var(--pattern-light) 100%);
  }
  .back-brand {
    position: absolute; right: 44px; bottom: 44px;
    display: flex; align-items: center; gap: 10px;
  }
  .brand-dot {
    width: 26px; height: 26px; border-radius: 50%;
    background: var(--brand-red);
  }
  .brand-name {
    font-weight: 700; font-size: 22px; letter-spacing: 1px;
    color: var(--brand-red); text-transform: uppercase;
  }
  .card--front { top: 468px; background: var(--white); }
  .front-brand {
    position: absolute; top: 62px; left: 0; right: 0;
    display: flex; justify-content: center; align-items: center; gap: 14px;
  }
  .front-brand .brand-dot { width: 62px; height: 62px; }
  .front-brand .brand-name { font-size: 30px; }
  .band-rule {
    position: absolute; left: 0; right: 0; top: 170px; height: 7px;
    background: var(--rule-grey);
  }
  .band {
    position: absolute; left: 0; right: 0; top: 177px; bottom: 0;
    background: var(--brand-red); color: var(--white);
  }
  .identity {
    position: absolute; right: 318px; top: 22px; text-align: right;
  }
  .identity__name { font-weight: 700; font-size: 25px; }
  .identity__title { font-size: 15px; margin-top: 2px; }
  .identity__address { font-size: 15px; line-height: 1.3; margin-top: 4px; }
  .divider {
    position: absolute; left: 298px; top: 26px; width: 2px; height: 110px;
    background: var(--white);
  }
  .contacts {
    position: absolute; left: 316px; top: 30px; list-style: none;
    font-size: 15px; line-height: 1.65;
  }
  .contacts li { display: flex; align-items: center; gap: 8px; }
  .contacts svg { width: 13px; height: 13px; fill: var(--white); flex: none; }
</style>
</head>
<body>

<section class="card card--back" aria-label="Card back">
  <div class="pattern-field" role="img" aria-label="Repeating tone-on-tone brand pattern"></div>
  <div class="back-brand">
    <span class="brand-dot"></span>
    <span class="brand-name">Dalvor Inc</span>
  </div>
</section>

<section class="card card--front" aria-label="Card front">
  <div class="front-brand">
    <span class="brand-dot"></span>
    <span class="brand-name">Dalvor Inc</span>
  </div>
  <div class="band-rule"></div>
  <div class="band">
    <div class="identity">
      <p class="identity__name">Alan Moreno</p>
      <p class="identity__title">President</p>
      <p class="identity__address">418 Birchfield Lane<br>Maple Hollow, MI 49012</p>
    </div>
    <div class="divider"></div>
    <ul class="contacts">
      <li><svg viewBox="0 0 16 16"><path d="M3.5 1l3 3-1.8 1.8c.9 2 2.5 3.6 4.5 4.5L11 8.5l3 3-2 2.5C6 13.5 2.5 10 1 4z"/></svg>555 214-3098</li>
      <li><svg viewBox="0 0 16 16"><path d="M4 0h8a1 1 0 0 1 1 1v14a1 1 0 0 1-1 1H4a1 1 0 0 1-1-1V1a1 1 0 0 1 1-1zm1 2v10h6V2zm3 11a1 1 0 1 0 0 2 1 1 0 0 0 0-2z"/></svg>555 870-4421</li>
      <li><svg viewBox="0 0 16 16"><path d="M0 3h16v10H0zm1.5 1.2V5l6.5 4 6.5-4v-.8L8 8z"/></svg>info@dalvorinc-example.com</li>
      <li><svg viewBox="0 0 16 16"><path d="M8 0a8 8 0 1 0 0 16A8 8 0 0 0 8 0zm0 1.5c.9 0 2 1.8 2.3 5.5H5.7C6 3.3 7.1 1.5 8 1.5zM1.6 8.5h2.6c.1 2 .5 3.7 1.1 4.9A6.5 6.5 0 0 1 1.6 8.5zm0-1.5a6.5 6.5 0 0 1 3.7-4.4C4.7 3.8 4.3 5.4 4.2 7zm4.1 1.5h4.6c-.3 3.7-1.4 6-2.3 6s-2-2.3-2.3-6zm6.1 0h2.6a6.5 6.5 0 0 1-3.7 4.9c.6-1.2 1-2.9 1.1-4.9zm0-1.5c-.1-1.6-.5-3.2-1.1-4.4A6.5 6.5 0 0 1 14.4 7z"/></svg>www.dalvorinc-example.com</li>
    </ul>
  </div>
</section>

</body>
</html>
```